Tall Oak Plumbing Company Wrap

Company logo and wrap
Phone number 804-555-0193
List of projects we handle
- water heater installation (gas, electric, tankless)
- sewer repair
- water main repair
- residential/light commercial plumbing
- drain cleaning
- bathroom/kitchen remodeling
- repair well systems
- fixture installation
- gas line services
- water filtration

Licensed and insured
Slogan "let the tall oaks handle it"
Clean work at affordable rates

Target Market(s)

30-75 homeowners

Industry/Entity Type

Plumbing

Colors
0054AA
0677BA
7BADD7
CADEEF
E8F1F8

Requirements
Must have
• Logo, phone number, licensed and insured, projects we handle

```html
<!DOCTYPE html>
<html lang="en">
<head>
<meta charset="utf-8">
<title>Tall Oak Plumbing Company Wrap</title>
<link rel="stylesheet" href="https://fonts.googleapis.com/css2?family=Russo+One&family=Open+Sans:wght@400;600&family=Montserrat:wght@700&display=swap">
<style>
  :root {
    --backdrop: #684d2b;
    --wrap-white: #ffffff;
    --brand-blue: #1f4fb0;
    --brand-navy: #1c2f78;
    --brand-mid: #0054aa;
    --brand-light: #7badd7;
    --brand-pale: #e8f1f8;
  }
  * { box-sizing: border-box; margin: 0; padding: 0; }
  html, body { width: 960px; height: 1200px; overflow: hidden; }
  body { background: var(--backdrop); font-family: "Open Sans", sans-serif; }
  .canvas { position: relative; width: 960px; height: 1200px; }

  .panel {
    position: absolute; left: 30px; width: 900px;
    background: var(--wrap-white); border-radius: 28px; overflow: hidden;
  }
  .panel--side { top: 60px; height: 420px; }
  .panel--rear { top: 580px; height: 560px; left: 150px; width: 660px; }

  .blue-sweep { position: absolute; inset: 0; }

  .contact { position: absolute; color: var(--wrap-white); white-space: nowrap; }
  .contact--side { left: 56px; top: 170px; }
  .phone { display: flex; align-items: center; gap: 10px; font-size: 30px; font-weight: 600; letter-spacing: .5px; }
  .phone svg { width: 26px; height: 26px; flex: none; }
  .web { font-size: 18px; font-weight: 600; margin-top: 4px; }

  .mascot {
    position: absolute;
    background: radial-gradient(circle at 45% 40%, var(--brand-light), var(--brand-blue) 70%);
    opacity: .35;
  }
  .mascot--side { left: 318px; top: 40px; width: 190px; height: 320px; border-radius: 95px; }
  .mascot--rear { left: 140px; top: 70px; width: 160px; height: 240px; border-radius: 80px; }

  .brand-name {
    position: absolute; font-family: "Russo One", sans-serif;
    color: var(--brand-navy); line-height: 1.05; text-transform: uppercase; white-space: nowrap;
  }
  .brand-name--side { left: 395px; top: 108px; font-size: 40px; }
  .brand-name--rear { left: 262px; top: 140px; font-size: 30px; }

  .slogan { position: absolute; color: var(--brand-navy); letter-spacing: 1px; white-space: nowrap; border-bottom: 2px solid var(--brand-navy); }
  .slogan--side { left: 397px; top: 252px; font-size: 15px; padding-bottom: 6px; width: 268px; }
  .slogan--rear { left: 264px; top: 248px; font-size: 13px; padding-bottom: 5px; width: 240px; }

  .credential { position: absolute; display: flex; align-items: center; gap: 6px; }
  .credential--side { left: 700px; top: 30px; }
  .credential--rear { left: 430px; top: 40px; transform: scale(.75); transform-origin: left top; }
  .credential svg { width: 52px; height: 62px; }
  .credential-labels { display: flex; flex-direction: column; gap: 3px; }
  .credential-label {
    background: var(--brand-navy); color: var(--wrap-white);
    font-size: 14px; padding: 1px 10px; text-align: center; letter-spacing: .5px;
  }

  .services {
    position: absolute; left: 686px; top: 132px; list-style: none;
    font-family: "Montserrat", sans-serif; font-size: 7.6px; color: var(--brand-mid);
    text-transform: uppercase; line-height: 1.85; white-space: nowrap;
  }
  .services li::before { content: "\2022"; margin-right: 3px; }

  .door-seam { position: absolute; left: 329px; top: 0; bottom: 0; width: 2px; background: var(--brand-pale); }
  .door-window { position: absolute; top: 20px; height: 210px; border: 2px solid var(--brand-light); border-radius: 18px; }
  .door-window--left { left: 20px; width: 290px; }
  .door-window--right { left: 350px; width: 290px; }
  .rear-contact {
    position: absolute; left: 0; right: 0; bottom: 40px;
    display: flex; justify-content: space-around; align-items: center; color: var(--brand-mid); font-weight: 600;
  }
  .rear-contact .phone { font-size: 26px; }
  .rear-contact .phone svg rect { fill: var(--brand-mid); }
  .rear-contact .web { font-size: 17px; margin-top: 0; }
</style>
</head>
<body>
<main class="canvas">

  <section class="panel panel--side" aria-label="Side wrap layout">
    <svg class="blue-sweep" viewBox="0 0 900 420" preserveAspectRatio="none" aria-hidden="true">
      <defs>
        <linearGradient id="sweep" x1="0" x2="1">
          <stop offset="0" stop-color="#14278a"/>
          <stop offset="1" stop-color="#2456bd"/>
        </linearGradient>
      </defs>
      <path d="M0 0 H540 C420 40 320 120 326 260 C330 340 340 390 348 420 H0 Z" fill="url(#sweep)"/>
    </svg>
    <div class="contact contact--side">
      <div class="phone">
        <svg viewBox="0 0 24 24" aria-hidden="true"><rect width="24" height="24" rx="5" fill="#fff"/><path d="M8 5l2 4-1.5 1.5a9 9 0 0 0 5 5L15 14l4 2-.8 3C12 19 5 12 5 5.8Z" fill="#1f4fb0"/></svg>
        804-555-0193
      </div>
      <div class="web">TallOakPlumbingVA.com</div>
    </div>
    <div class="mascot mascot--side" role="img" aria-label="Illustration of a plumber carrying a large pipe wrench inside a circular frame"></div>
    <h1 class="brand-name brand-name--side">Tall Oak<br>Plumbing<br>Company</h1>
    <p class="slogan slogan--side">Let the Tall Oaks handle it</p>
    <div class="credential credential--side">
      <svg viewBox="0 0 52 62" aria-hidden="true"><path d="M26 2 L50 12 V30 C50 46 38 56 26 60 C14 56 2 46 2 30 V12 Z" fill="#1c2f78"/></svg>
      <div class="credential-labels">
        <span class="credential-label">LICENSED</span>
        <span class="credential-label">INSURED</span>
      </div>
    </div>
    <ul class="services">
      <li>Water heater installation</li>
      <li>Sewer repair</li>
      <li>Water main repair</li>
      <li>Residential/light commercial plumbing</li>
      <li>Drain cleaning</li>
      <li>Bathroom/kitchen remodeling</li>
      <li>Repair well systems</li>
      <li>Fixture installation</li>
      <li>Gas line services</li>
      <li>Water filtration</li>
    </ul>
  </section>

  <section class="panel panel--rear" aria-label="Rear doors wrap layout">
    <div class="door-window door-window--left"></div>
    <div class="door-window door-window--right"></div>
    <div class="door-seam"></div>
    <div class="mascot mascot--rear" role="img" aria-label="Illustration of a plumber carrying a large pipe wrench inside a circular frame"></div>
    <h2 class="brand-name brand-name--rear">Tall Oak<br>Plumbing<br>Company</h2>
    <p class="slogan slogan--rear">Let the Tall Oaks handle it</p>
    <div class="credential credential--rear">
      <svg viewBox="0 0 52 62" aria-hidden="true"><path d="M26 2 L50 12 V30 C50 46 38 56 26 60 C14 56 2 46 2 30 V12 Z" fill="#1c2f78"/></svg>
      <div class="credential-labels">
        <span class="credential-label">LICENSED</span>
        <span class="credential-label">INSURED</span>
      </div>
    </div>
    <div class="rear-contact">
      <div class="phone">
        <svg viewBox="0 0 24 24" aria-hidden="true"><rect width="24" height="24" rx="5"/><path d="M8 5l2 4-1.5 1.5a9 9 0 0 0 5 5L15 14l4 2-.8 3C12 19 5 12 5 5.8Z" fill="#fff"/></svg>
        804-555-0193
      </div>
      <div class="web">TallOakPlumbingVA.com</div>
    </div>
  </section>

</main>
</body>
</html>
```